Brochure Projecct

I need a brochure created for my company, which will be sent to customers via email in PDF format. I have uploaded the company logo with this project, which I want incorporated in the design.

Designers should view the company website at www.brightcounselpages.com. I want the brochure to compliment the website (i.e., very clean design). I would also like pictures added to the brochure to make the design visually stunning.

In terms of content, I need four pages in the brochure to add four separate sections of content (one section per page). The four sections of content will be as follows (1) Search Engine Optimization Benefits (2) Increased Client Retention (3) Showcase Your Law Firm (4) Maximize Your Online ROI (5) Pricing Plans. I will give the content to the winning designer to add to the project. Each individual content section will have four subsection titles after which content of approximately 100 to 200 words will appear.

Designers can decide if other pages should be added to the brochure (i.e., a "cover page" that would have little content, but be visually appealing like the cover of a book - - - a "back page" that may just have the logo, contact information, etc).

My company address and email address should be prominently featured through every page (address: 2715 West Juniper Avenue, Suite 1400, Scottsdale, Arizona 85317; email: sales@brightcounselpages.com).

Industry/Entity Type

It Company

Requirements
Must have
• Clean look but visually stunning incorporating the design of the website at brightcounselpages.com as well as the logo. Also, room for content as set forth in the description of this project.

```html
<!DOCTYPE html>
<html lang="en">
<head>
<meta charset="utf-8">
<title>Bright Counsel Pages – Brochure</title>
<link href="https://fonts.googleapis.com/css2?family=Arimo:wght@400;700&display=swap" rel="stylesheet">
<style>
:root{
  --navy:#24508f;
  --cyan:#0aaae9;
  --ink:#1d2438;
  --paper:#ffffff;
  --mist:#eef1f4;
  --stone:#c9c2b6;
}
*{box-sizing:border-box;margin:0;padding:0}
html,body{width:1200px;height:1000px;overflow:hidden;background:var(--paper)}
body{position:relative;font-family:"Arimo",Arial,sans-serif;color:var(--ink)}
.sheet{position:absolute;left:313px;width:606px;overflow:hidden;background:var(--paper)}
.sheet--outer{top:30px;height:446px}
.sheet--inner{top:508px;height:445px}
.band{position:absolute;left:0;width:100%;background:linear-gradient(90deg,var(--navy) 0%,#1577b8 50%,var(--cyan) 100%)}
.band--head{top:0;height:43px}
.band--foot{bottom:0}
.sheet--outer .band--foot{height:61px}
.sheet--inner .band--foot{height:60px;opacity:.85}
.section-title{position:absolute;top:20px;font-size:8.4px;font-weight:700;color:#fff}
.backdrop{position:absolute}
.sheet--outer .backdrop{left:0;top:43px;width:403px;height:342px;
  background:radial-gradient(ellipse at 55% 40%,#d8dbe0 0%,#eceef1 45%,#f8f9fa 80%)}
.sheet--inner .backdrop{left:0;top:43px;width:100%;height:402px;
  background:linear-gradient(135deg,#ece9e3 0%,#d6d0c5 40%,#bfb8ab 65%,#e3e0da 100%)}
.sheet--inner .veil{position:absolute;left:0;top:43px;width:100%;height:342px;background:rgba(255,255,255,.55)}
.column{position:absolute;width:180px;font-size:6.9px;line-height:10.2px}
.column p+p{margin-top:6px}
.price-label{margin-top:32px}
.footer-address{position:absolute;width:180px;text-align:center;font-size:6.2px;line-height:9.6px;font-weight:700;color:#fff}
.sheet--outer .footer-address{top:403px}
.sheet--inner .footer-address{top:401px}
.brand{position:absolute;left:403px;top:43px;width:203px;height:142px;background:var(--paper);
  display:flex;align-items:center;justify-content:center;gap:8px}
.brand-mark{width:22px;height:22px;border-radius:50%;background:var(--cyan)}
.brand-name{font-size:17px;font-weight:700;color:var(--navy);line-height:19px}
.photo{position:absolute;left:403px;top:185px;width:203px;height:200px;
  background:linear-gradient(160deg,#c9d3dc 0%,#7d8c99 45%,#2c3440 100%)}
</style>
</head>
<body>

<section class="sheet sheet--outer">
  <div class="backdrop" role="img" aria-label="Faded photo of a fountain pen signing a contract"></div>
  <div class="band band--head"></div>
  <h2 class="section-title" style="left:20px">Search Engine Optimization Benefits</h2>
  <h2 class="section-title" style="left:216px">Pricing Plans</h2>

  <div class="column" style="left:20px;top:54px">
    <p>Ihillorem que aut et untio ipidemquiam iliquisciet velesto totaspelique voloreptae es re sit lit que nesequi ut etures est, optatibea digendit, imus mos sam utem utem. Henti aut que sunt harum inverov itiaesendae. Fuga. Nem quiaepedi dellacestrum volupta speliqui consequ aestiore pa nullore explam, et optaquatio. Tem qui aciassequid et volum dolecto ex essitis eostrum dusamus experupit aceria quid que doluptatus doluptur, quis consedit il ipsanih iciatur aut exero voluptae offictist lam sum licture heniet evernat.</p>
    <p>Um quatem utas adiatiae ex eiur, qui dolupta tempos quos arcias alicta aut estinvent.</p>
    <p>Vitin et, que es experspel il minis mo consequas dolore in rest ent ium ium fugianis et hilibust, si aut min plit fuga. Erepe nobit quas alignis es et earum ut res et rem illorer sperfero cor acepe que et quiatem quis cuscias sincipsam quis ipsam, volorec tasimaximet odit es nobis et omni odi comnimin rem quide occum</p>
  </div>

  <div class="column" style="left:216px;top:54px">
    <p>Ihillorem que aut et untio ipidemquiam iliquisciet velesto totaspelique voloreptae es re sit lit que nesequi ut etures est, optatibea digendit, imus mos sam utem utem. Henti aut que sunt harum inverov itiaesendae. Fuga. Nem quiaepedi dellacestrum volupta speliqui consequ aestiore pa nullore explam, et optaquatio. Tem qui aciassequid</p>
    <p class="price-label">Price</p>
  </div>

  <div class="brand">
    <span class="brand-mark"></span>
    <span class="brand-name">Bright Counsel<br>Pages</span>
  </div>
  <div class="photo" role="img" aria-label="Photo of business people shaking hands over a laptop in an office"></div>

  <div class="band band--foot"></div>
  <p class="footer-address" style="left:0">2715 West Juniper Avenue, Suite 1400,<br>Scottsdale, Arizona 85317<br>Email: sales@brightcounselpages.com</p>
  <p class="footer-address" style="left:212px">2715 West Juniper Avenue, Suite 1400,<br>Scottsdale, Arizona 85317<br>Email: sales@brightcounselpages.com</p>
  <p class="footer-address" style="left:414px">2715 West Juniper Avenue, Suite 1400,<br>Scottsdale, Arizona 85317<br>Email: sales@brightcounselpages.com</p>
</section>

<section class="sheet sheet--inner">
  <div class="backdrop" role="img" aria-label="Photo of a gavel and glasses resting on legal documents"></div>
  <div class="veil"></div>
  <div class="band band--head"></div>
  <h2 class="section-title" style="left:20px">Increased Client Retention</h2>
  <h2 class="section-title" style="left:216px">Showcase Your Law Firm</h2>
  <h2 class="section-title" style="left:411px">Maximize Your Online ROI</h2>

  <div class="column" style="left:20px;top:53px">
    <p>Ihillorem que aut et untio ipidemquiam iliquisciet velesto totaspelique voloreptae es re sit lit que nesequi ut etures est, optatibea digendit, imus mos sam utem utem. Henti aut que sunt harum inverov itiaesendae. Fuga. Nem quiaepedi dellacestrum volupta speliqui consequ aestiore pa nullore explam, et optaquatio. Tem qui aciassequid et volum dolecto ex essitis eostrum dusamus experupit aceria quid que doluptatus doluptur, quis consedit il ipsanih iciatur aut exero voluptae offictist lam sum licture heniet evernat.</p>
    <p>Um quatem utas adiatiae ex eiur, qui dolupta tempos quos arcias alicta aut estinvent.</p>
    <p>Vitin et, que es experspel il minis mo consequas dolore in rest ent ium ium fugianis et hilibust, si aut min plit fuga. Erepe nobit quas alignis es et earum ut res et rem illorer sperfero cor acepe que et quiatem quis cuscias sincipsam quis ipsam, volorec tasimaximet odit es nobis et omni odi comnimin rem quide occum arcia quam fugia di corrum que dolectur asit facernam, offic tet quunt, optatur, num quatus volore explam aut optio. Nem et ut acearch illorum quiam labori dolo etus, quam audi non re prem. Nostiunt et etur? Ehendam et voluptae volupta volor asperum everit quo volorit eos et ullautem veliqua temperum as sim re elent.</p>
  </div>

  <div class="column" style="left:216px;top:53px">
    <p>Ihillorem que aut et untio ipidemquiam iliquisciet velesto totaspelique voloreptae es re sit lit que nesequi ut etures est, optatibea digendit, imus mos sam utem utem. Henti aut que sunt harum inverov itiaesendae. Fuga. Nem quiaepedi dellacestrum volupta speliqui consequ aestiore pa nullore explam, et optaquatio. Tem qui aciassequid et volum dolecto ex essitis eostrum dusamus experupit aceria quid que doluptatus doluptur, quis consedit il ipsanih iciatur aut exero voluptae offictist lam sum licture heniet evernat.</p>
    <p>Um quatem utas adiatiae ex eiur, qui dolupta tempos quos arcias alicta aut estinvent.</p>
    <p>Vitin et, que es experspel il minis mo consequas dolore in rest ent ium ium fugianis et hilibust, si aut min plit fuga. Erepe nobit quas alignis es et earum ut res et rem illorer sperfero cor acepe que et quiatem quis cuscias sincipsam quis ipsam, volorec tasimaximet odit es nobis et omni odi comnimin rem quide occum arcia quam fugia di corrum que dolectur asit facernam, offic tet quunt, optatur, num quatus volore explam aut optio. Nem et ut acearch illorum quiam labori dolo etus, quam audi non re prem. Nostiunt et etur? Ehendam et voluptae volupta volor asperum everit quo volorit eos et ullautem</p>
  </div>

  <div class="column" style="left:411px;top:53px">
    <p>Ihillorem que aut et untio ipidemquiam iliquisciet velesto totaspelique voloreptae es re sit lit que nesequi ut etures est, optatibea digendit, imus mos sam utem utem. Henti aut que sunt harum inverov itiaesendae. Fuga. Nem quiaepedi dellacestrum volupta speliqui consequ aestiore pa nullore explam, et optaquatio. Tem qui aciassequid et volum dolecto ex essitis eostrum dusamus experupit aceria quid que doluptatus doluptur, quis consedit il ipsanih iciatur aut exero voluptae offictist lam sum licture heniet evernat.</p>
    <p>Um quatem utas adiatiae ex eiur, qui dolupta tempos quos arcias alicta aut estinvent.</p>
    <p>Vitin et, que es experspel il minis mo consequas dolore in rest ent ium ium fugianis et hilibust, si aut min plit fuga. Erepe nobit quas alignis es et earum ut res et rem illorer sperfero cor acepe que et quiatem quis cuscias sincipsam quis ipsam, volorec tasimaximet odit es nobis et omni odi comnimin rem quide occum arcia quam fugia di corrum que dolectur asit facernam, offic tet quunt, optatur, num quatus volore explam aut optio. Nem et ut acearch illorum quiam labori dolo etus, quam audi non re prem. Nostiunt et etur? Ehendam et voluptae volupta volor asperum everit quo volorit eos et ullautem veliqua temperum as sim re elent.</p>
  </div>

  <div class="band band--foot"></div>
  <p class="footer-address" style="left:0">2715 West Juniper Avenue, Suite 1400,<br>Scottsdale, Arizona 85317<br>Email: sales@brightcounselpages.com</p>
  <p class="footer-address" style="left:212px">2715 West Juniper Avenue, Suite 1400,<br>Scottsdale, Arizona 85317<br>Email: sales@brightcounselpages.com</p>
  <p class="footer-address" style="left:414px">2715 West Juniper Avenue, Suite 1400,<br>Scottsdale, Arizona 85317<br>Email: sales@brightcounselpages.com</p>
</section>

</body>
</html>
```